Restaurant DIGITAL menu design- menu items name and description typed in already

Menu design for vietnamese sandwich restaurant menu board. Design will be used in 6 feet tall by 4 feet wide format on four 4k tv mounted VERTICALLY. Main colours of design yellow, white, black. Design should be FUN AND CASUAL.

Target Market(s)

Young professionals in 30-40s age group

Requirements
Must have
• Please note that this is FOUR 4K tv mounted VERTICALLY. Two on top, two on bottom VERTICALLY. All horizontal design will NOT be considered as winner.

Please use menu information in "MAIN FILE" for design, no generic or incorrect information.

No stock photos, free or pay
Link for more images

https://www.pelmorbox.net/sh/qr3t8kwzeh4m52x/BQLT_9PRwNcY7hkkj2ZsTfLmm?dl=0
Should not have
• HORIZONTAL DESIGN WILL NOT BE CONSIDERED.
No Stock photos.

```html
<!DOCTYPE html>
<html lang="en">
<head>
<meta charset="utf-8">
<title>Ravo Banh Mi – Menu Board</title>
<link href="https://fonts.googleapis.com/css2?family=Fjalla+One&family=Open+Sans:ital,wght@0,400;0,700;1,400&display=swap" rel="stylesheet">
<style>
:root{
  --yellow:#f7c51e;
  --orange:#f39a1c;
  --brown:#4a2c17;
  --ink:#1d1d1b;
  --grey:#6b6b6b;
  --white:#ffffff;
  --page:#f3f0ea;
  --band-warm:#fdf0c2;
  --band-tan:#efe3d3;
}
*{box-sizing:border-box;margin:0;padding:0}
html,body{width:800px;height:1200px;overflow:hidden;background:var(--page)}
body{position:relative;font-family:"Open Sans",Arial,sans-serif;color:var(--ink)}
.panel{position:absolute;width:394px;height:594px;background:var(--white);border:11px solid var(--yellow);padding:12px 22px;overflow:hidden}
.panel--tl{left:2px;top:2px}
.panel--tr{left:404px;top:2px;border-color:var(--brown)}
.panel--bl{left:2px;top:604px}
.panel--br{left:404px;top:604px;border-color:var(--brown)}
.heading{font-family:"Fjalla One",Impact,sans-serif;font-size:24px;letter-spacing:.5px;text-align:center;color:var(--orange);line-height:1.1;margin:10px 0 8px}
.panel--tr .heading,.panel--br .heading{color:var(--brown)}
.band{background:var(--band-warm);padding:4px 0;margin:12px -22px 10px}
.band--first{margin-top:0}
.panel--tr .band,.panel--br .band{background:var(--band-tan)}
.item{display:flex;justify-content:space-between;align-items:flex-start;margin-bottom:7px}
.item__name{font-family:"Fjalla One",Impact,sans-serif;font-size:13px;letter-spacing:.3px;line-height:1.15}
.item__desc{font-size:7px;font-style:italic;color:var(--grey);line-height:1.3}
.item__price{font-family:"Fjalla One",Impact,sans-serif;font-size:13px;padding-left:10px;flex:none}
.photo{display:block}
.photo--drinks{height:150px;margin:-12px -22px 0;background:linear-gradient(160deg,#fde7a0 0%,#f6b64a 45%,#e96a6a 75%,#6fb7c9 100%)}
.photo--sandwich{position:absolute;left:0;right:0;bottom:0;height:105px;background:linear-gradient(180deg,#f4e3c1 0%,#d9a45c 45%,#8fb860 70%,#c9834a 100%)}
.photo--bowl{width:140px;height:120px;flex:none;border-radius:4px;background:radial-gradient(circle at 50% 50%,#c7d98a 0%,#7ea84a 40%,#5a3b26 75%,#2a1e15 100%)}
.photo--snacks{position:absolute;left:0;right:0;bottom:0;height:95px;background:linear-gradient(180deg,#f2e6cf 0%,#e4b16a 40%,#a9c774 70%,#d8874f 100%)}
.addons{display:flex;gap:14px}
.addons__list{flex:1}
.addons__list .band{margin:0 -22px 8px 0}
.addons__list .item{margin-bottom:3px}
.bowls__intro{font-size:7px;font-style:italic;color:var(--grey);text-align:center;margin:-4px 0 6px}
.bowls__label{font-family:"Fjalla One",Impact,sans-serif;font-size:12px;margin-bottom:2px}
.bowls__opt{font-family:"Fjalla One",Impact,sans-serif;font-size:12px;line-height:1.35}
.snacks .item{margin-bottom:3px}
</style>
</head>
<body>

<section class="panel panel--tl">
  <div class="photo photo--drinks" role="img" aria-label="Colourful tropical juice drinks in glasses"></div>
  <h2 class="heading">FRESH JUICES</h2>
  <div class="item"><div><div class="item__name">GOOD MORNING: AN A.M. JUICE</div><div class="item__desc">apple / carrot / lemon / ginger</div></div><div class="item__price">6</div></div>
  <div class="item"><div><div class="item__name">GREEN GODDESS</div><div class="item__desc">kale / cucumber / green apple / pear / lemon</div></div><div class="item__price">6</div></div>
  <div class="item"><div><div class="item__name">REVITALIZE</div><div class="item__desc">beet / carrot / lemon / ginger</div></div><div class="item__price">6</div></div>
  <div class="item"><div><div class="item__name">POWER-UP</div><div class="item__desc">orange / lemon / ginger / agave</div></div><div class="item__price">6</div></div>
  <div class="item"><div><div class="item__name">RAVO SIGNATURE</div><div class="item__desc">mango / passion fruit / pineapple / lime</div></div><div class="item__price">6</div></div>
  <h2 class="heading band">JUICE BOOST</h2>
  <div class="item"><div><div class="item__name">SUPERSEED BLEND (WITH COCONUT)</div><div class="item__desc">a boost of ground flax, chia and hemp seed</div></div><div class="item__price">0.75</div></div>
  <div class="item"><div><div class="item__name">FLAXSEED WITH MIXED BERRIES</div><div class="item__desc">a boost of ground flax and mixed berries</div></div><div class="item__price">0.50</div></div>
</section>

<section class="panel panel--tr">
  <h2 class="heading band band--first">SPECIALTY COFFEE</h2>
  <div class="item"><div><div class="item__name">CA PHE SUA DA</div><div class="item__desc">vietnamese coffee / sweetened condensed milk</div></div><div class="item__price">4.0</div></div>
  <div class="item"><div><div class="item__name">CA PHE DANH DA</div><div class="item__desc">vietnamese coffee / ice</div></div><div class="item__price">4.0</div></div>
  <div class="item"><div><div class="item__name">PANDAN ICED LATTE</div><div class="item__desc">vietnamese coffee / pandan / coconut milk</div></div><div class="item__price">5.5</div></div>
  <div class="item"><div><div class="item__name">UBE ICED LATTE</div><div class="item__desc">vietnamese coffee / ube / coconut milk</div></div><div class="item__price">5.5</div></div>
  <div class="item"><div><div class="item__name">AVOCADO WAKE-UP SHAKE</div><div class="item__desc">avocado / coffee / condensed milk</div></div><div class="item__price">6.0</div></div>
  <h2 class="heading band">FRESH BREWED TEA</h2>
  <div class="item"><div><div class="item__name">JASMINE</div><div class="item__desc">high mountain green tea</div></div><div class="item__price">3.0</div></div>
  <div class="item"><div><div class="item__name">OOLONG</div><div class="item__desc">roasted oolong, hot or iced</div></div><div class="item__price">3.0</div></div>
  <div class="item"><div><div class="item__name">IMPERIAL PU ERH</div><div class="item__desc">aged dark tea, hot or iced</div></div><div class="item__price">3.0</div></div>
  <h2 class="heading band">KID'S (12 &amp; UNDER)</h2>
  <div class="item"><div><div class="item__name">BANH MI KID MEAL</div><div class="item__desc">choice of half traditional banh mi, apple juice or chocolate milk</div></div><div class="item__price">6</div></div>
</section>

<section class="panel panel--bl">
  <h2 class="heading band band--first">RAVO INSPIRED FARE</h2>
  <div class="item"><div><div class="item__name">CHAR SIU XIU MAI BANH MI</div><div class="item__desc">bbq pork, pork dumpling, pickled veg, cilantro</div></div><div class="item__price">9</div></div>
  <div class="item"><div><div class="item__name">PHO FRENCH DIP BANH MI</div><div class="item__desc">shaved beef brisket, pho broth, herbs, jalapeno</div></div><div class="item__price">9</div></div>
  <div class="item"><div><div class="item__name">BEEF RENDANG BANH MI</div><div class="item__desc">slow braised beef, cucumber, pickled veg, cilantro</div></div><div class="item__price">8</div></div>
  <div class="item"><div><div class="item__name">CURRY CHICKEN BANH MI</div><div class="item__desc">curry chicken, cucumber, pickled veg, cilantro</div></div><div class="item__price">7.5</div></div>
  <div class="item"><div><div class="item__name">LUNCHEON MEAT &amp; EGG BANH MI</div><div class="item__desc">luncheon meat, fried egg, cucumber, pickled veg</div></div><div class="item__price">6.5</div></div>
  <h2 class="heading band">TRADITIONAL FARE</h2>
  <div class="item"><div><div class="item__name">SPECIAL COLD CUT COMBO BANH MI</div><div class="item__desc">pork roll, ham, pate, cucumber, pickled veg</div></div><div class="item__price">7</div></div>
  <div class="item"><div><div class="item__name">LEMONGRASS PORK BANH MI</div><div class="item__desc">grilled pork, cucumber, pickled veg, jalapeno</div></div><div class="item__price">7</div></div>
  <div class="item"><div><div class="item__name">LEMONGRASS CHICKEN BANH MI</div><div class="item__desc">grilled chicken, cucumber, pickled veg, jalapeno</div></div><div class="item__price">7</div></div>
  <div class="item"><div><div class="item__name">CRISPY SEASONED TOFU BANH MI</div><div class="item__desc">crispy tofu, cucumber, pickled veg, cilantro</div></div><div class="item__price">7</div></div>
  <div class="photo photo--sandwich" role="img" aria-label="Row of banh mi sandwiches"></div>
</section>

<section class="panel panel--br">
  <div class="addons">
    <div class="photo photo--bowl" role="img" aria-label="Vermicelli bowl with grilled meat and herbs"></div>
    <div class="addons__list">
      <h2 class="heading band">ADD-ONS</h2>
      <div class="item"><div class="item__name">EGG ROLL (1)</div><div class="item__price">1.75</div></div>
      <div class="item"><div class="item__name">FRIED EGG</div><div class="item__price">1.5</div></div>
      <div class="item"><div class="item__name">GARLIC AIOLI</div><div class="item__price">1.0</div></div>
      <div class="item"><div class="item__name">HOUSE MADE PATE</div><div class="item__price">1.0</div></div>
      <div class="item"><div class="item__name">EXTRA MEAT</div><div class="item__price">2.5</div></div>
    </div>
  </div>
  <h2 class="heading band">BOWLS</h2>
  <p class="bowls__intro">All bowls served with lettuce, tomatoes, cilantro, mint, cucumber and pickled veg</p>
  <div class="item"><div>
    <div class="bowls__label">CHOOSE:</div>
    <div class="bowls__opt">SALAD BOWL, VERMICELLI BOWL, RICE BOWL</div>
    <div class="bowls__opt">GRILLED LEMONGRASS PORK</div>
    <div class="bowls__opt">GRILLED LEMONGRASS CHICKEN</div>
    <div class="bowls__opt">CRISPY SEASONED TOFU</div>
  </div><div class="item__price">11</div></div>
  <div class="snacks">
    <h2 class="heading band">SNACKS</h2>
    <div class="item"><div class="item__name">CHILI CRAB RANGOON (3)</div><div class="item__price">5.5</div></div>
    <div class="item"><div class="item__name">VIETNAMESE PORK EGG ROLLS (2)</div><div class="item__price">3.5</div></div>
    <div class="item"><div class="item__name">VEGGIE EGG ROLLS (2)</div><div class="item__price">3.5</div></div>
    <div class="item"><div class="item__name">MANGO PAPAYA SHRIMP SPRING ROLLS (2)</div><div class="item__price">5.5</div></div>
    <div class="item"><div class="item__name">SHRIMP CHIPS</div><div class="item__price">2.5</div></div>
  </div>
  <div class="photo photo--snacks" role="img" aria-label="Banh mi with egg rolls and spring rolls"></div>
</section>

</body>
</html>
```